Book cover for a racy book called: A Starling's Manual For Finding Sparkle In Midlife Dating

Cover for book called, "A Starling's Manual For Finding Sparkle In Midlife Dating" I'd like it to be edgy sexy and provocative. It's a silky leg with a killer stiletto getting out of a car door. It is a guy kissing the back of the neck of a woman. It is four women's hands toasting with martinis. Written by MarisolAnn Quenby

Reason: New ideas for the cover! It's a silky leg with a killer stiletto getting out of a car door. It is a guy kissing the back of the neck of a woman. It is four women's hands toasting with martinis.

Target Market(s)

Women ages 35-60

Font styles to use
Serif
Sans Serif
Other font styles liked:
• Hattori Hanzo

Requirements
Must have
• It's a silky leg with a killer stiletto getting out of a car door. It is a guy kissing the back of the neck of a woman. It is four women's hands toasting with martinis. Edgy sexy vibe. I need a great artsy graphic using my face or entire body either with my picture or a characature of me. Lettering should reflect hot topics to grab attention. Title and author need to be prominant. Choose any of the pictures attached to sketch or characature.
Nice to have
• Get single women's opinions as to what they'd most likely pick up in a book store. The idea is to get the inspiration that any woman of any shape can look hot, sexy and confident without looking too young or slutty.
Should not have
• No picture of a cougar, would rather see confidence and sexy woman that any woman can become

```html
<!DOCTYPE html>
<html lang="en">
<head>
<meta charset="utf-8">
<title>A Starling's Manual For Finding Sparkle In Midlife Dating — Cover Options</title>
<link rel="stylesheet" href="https://fonts.googleapis.com/css2?family=Almendra+Display&family=Bebas+Neue&family=Lobster&family=Oranienbaum&family=Cinzel:wght@900&family=Germania+One&family=Pathway+Gothic+One&display=swap">
<style>
  :root {
    --page: #ffffff;
    --ink-black: #111111;
    --band-dark: #5a1512;
    --band-mid: #8e1f1a;
    --band-bright: #d4302a;
    --swirl-green: #4fd27a;
    --swirl-magenta: #c0326e;
    --swirl-slate: #55607a;
    --swirl-teal: #8fe0e0;
    --swirl-olive: #8a8a3a;
    --figure-tone: #2a2224;
    --figure-tone-soft: #3a3032;
    --chrome-light: #eef6ff;
    --chrome-mid: #7fa8e8;
    --chrome-deep: #2a4fa0;
    --title-white: #ffffff;
  }
  * { margin: 0; padding: 0; box-sizing: border-box; }
  html, body { width: 848px; height: 1200px; overflow: hidden; background: var(--page); }
  .sheet { position: relative; width: 848px; height: 1200px; }

  .cover { position: absolute; overflow: hidden; background: var(--band-mid); }
  .cover--a { left: 41px; top: 46px; width: 369px; height: 522px; }
  .cover--b { left: 432px; top: 44px; width: 370px; height: 524px; }
  .cover--c { left: 41px; top: 621px; width: 371px; height: 525px; }
  .cover--d { left: 432px; top: 616px; width: 374px; height: 530px; }

  .cover__topbar { position: absolute; left: 0; right: 0; top: 0; height: 16px; background: var(--ink-black); }
  .cover__author-band, .cover__base-band {
    position: absolute; left: 0; right: 0;
    background: linear-gradient(90deg, var(--band-dark) 0%, var(--band-mid) 55%, var(--band-bright) 100%);
  }
  .cover__author-band { top: 16px; height: 103px; }
  .cover__base-band { top: 418px; bottom: 0; }

  .cover__art {
    position: absolute; left: 0; right: 0; top: 119px; height: 299px;
    background:
      radial-gradient(ellipse 30% 35% at 48% 42%, rgba(70,80,110,.9), transparent 70%),
      conic-gradient(from 200deg at 52% 42%,
        var(--swirl-slate), var(--swirl-green), var(--swirl-magenta), var(--swirl-teal),
        var(--band-bright), var(--band-mid), var(--swirl-olive), var(--swirl-green), var(--swirl-slate));
  }

  .cover__figure {
    position: absolute; left: 40%; width: 37%; top: 6%; bottom: -40%;
    border-radius: 24px;
    background: linear-gradient(180deg, var(--figure-tone-soft), var(--figure-tone));
    opacity: .85;
  }
  .cover--a .cover__figure { left: 42%; }

  .cover__author {
    position: absolute; left: 0; right: 0; top: 40px;
    text-align: center; white-space: nowrap; font-weight: 400;
    background: linear-gradient(180deg, var(--chrome-light) 0%, var(--chrome-mid) 45%, var(--chrome-deep) 60%, var(--chrome-light) 100%);
    -webkit-background-clip: text; background-clip: text; color: transparent;
    filter: drop-shadow(2px 2px 1px rgba(0,0,0,.75));
  }
  .cover--a .cover__author { font-family: "Almendra Display", serif; font-size: 36px; top: 42px; }
  .cover--b .cover__author { font-family: "Bebas Neue", sans-serif; font-size: 42px; top: 38px; letter-spacing: 0; word-spacing: 14px; }
  .cover--c .cover__author { font-family: "Lobster", cursive; font-size: 38px; top: 40px; }
  .cover--d .cover__author { font-family: "Oranienbaum", serif; font-size: 44px; top: 36px; }

  .cover__title {
    position: absolute; left: 0; right: 0; text-align: center; font-weight: 400;
    color: var(--title-white); text-transform: uppercase;
    text-shadow: 2px 2px 2px rgba(0,0,0,.85), 0 0 6px rgba(0,0,0,.5);
  }
  .cover--a .cover__title { font-family: "Cinzel", serif; font-weight: 900; font-size: 21px; line-height: 33px; top: 370px; }
  .cover--b .cover__title { font-family: "Germania One", sans-serif; font-size: 23px; line-height: 36px; top: 358px; letter-spacing: 1px; }
  .cover--c .cover__title, .cover--d .cover__title { font-family: "Pathway Gothic One", sans-serif; font-size: 28px; line-height: 36px; }
  .cover--c .cover__title { top: 367px; }
  .cover--d .cover__title { top: 372px; }
</style>
</head>
<body>
<main class="sheet">
  <section class="cover cover--a">
    <div class="cover__topbar"></div>
    <div class="cover__author-band"></div>
    <div class="cover__art"></div>
    <div class="cover__base-band"></div>
    <div class="cover__art-slot" style="position:absolute;left:0;right:0;top:119px;height:403px;overflow:hidden"><div class="cover__figure" role="img" aria-label="Caricature of the author standing, hands on hips, in a black dress and heels"></div></div>
    <h2 class="cover__author">MarisolAnn Quenby</h2>
    <h1 class="cover__title">A Starling's Manual<br>For Finding<br>Sparkle in Midlife<br>Dating</h1>
  </section>

  <section class="cover cover--b">
    <div class="cover__topbar"></div>
    <div class="cover__author-band"></div>
    <div class="cover__art"></div>
    <div class="cover__base-band"></div>
    <div class="cover__art-slot" style="position:absolute;left:0;right:0;top:119px;height:405px;overflow:hidden"><div class="cover__figure" role="img" aria-label="Caricature of the author standing, hands on hips, in a black dress and heels"></div></div>
    <h2 class="cover__author">MarisolAnn Quenby</h2>
    <h1 class="cover__title">A Starling's Manual<br>For Finding<br>Sparkle in Midlife<br>Dating</h1>
  </section>

  <section class="cover cover--c">
    <div class="cover__topbar"></div>
    <div class="cover__author-band"></div>
    <div class="cover__art"></div>
    <div class="cover__base-band"></div>
    <div class="cover__art-slot" style="position:absolute;left:0;right:0;top:119px;height:406px;overflow:hidden"><div class="cover__figure" role="img" aria-label="Caricature of the author standing, hands on hips, in a black dress and heels"></div></div>
    <h2 class="cover__author">MarisolAnn Quenby</h2>
    <h1 class="cover__title">A Starling's Manual<br>For Finding Sparkle<br>In Midlife Dating</h1>
  </section>

  <section class="cover cover--d">
    <div class="cover__topbar"></div>
    <div class="cover__author-band"></div>
    <div class="cover__art"></div>
    <div class="cover__base-band"></div>
    <div class="cover__art-slot" style="position:absolute;left:0;right:0;top:119px;height:411px;overflow:hidden"><div class="cover__figure" role="img" aria-label="Caricature of the author standing, hands on hips, in a black dress and heels"></div></div>
    <h2 class="cover__author">MarisolAnn Quenby</h2>
    <h1 class="cover__title">A Starling's Manual<br>For Finding Sparkle<br>In Midlife Dating</h1>
  </section>
</main>
</body>
</html>
```